Emergency Vehicle Installer and Security Firm Needs a Business Card

Our company "Corvalt" need a business card for our Emergency Vehicle Equipment Installation and Infrastructure Security Business. We are contract designers, manufacturers and installers for Emergency Vehicle Fleets. This includes installation of Emergency Lights, Sirens, Vehicle Graphics and Radio Communications. We also supply this products to an international market. We also do consultant, and installation of high level security access, alarm and surveillance equipment for medium to large size businesses.

The design should represent a level of trust in our professionalism and expertise. It should visually display our ongoing relationship with the emergency services, but not overtake our commitment to high level security options.

Target Market(s)

Emergency Services and Businesses requiring high level security

Industry/Entity Type

Business

Contact Information for Business Card

*note complete details will be given to the winning designer for revising. The name "Mark Pell will be used to fill in name".

Mark Pell
Managing Director
Corvalt NZ Limited
Phone: +64 027 604 91352
Email: mark.pell@corvalt-example.co.nz

Requirements
Must have
• Card must be in black. Using our logo on the top as supplied. Designers should try having the reverse side as a blurred image of police lights (red and blue) with our logo in greyscale in the centre (this is not particularly a requirement, but feel free to play around with this option).
Nice to have
• A card design that looks good when spot UV printed. A clean compact and graphic design. A grey scale feel on the front (excluding logo, but you can play around with that idea). Rounded smooth text.
Should not have
• Will update this section as designs come through - feel free to submit what you feel would look good.

```html
<!DOCTYPE html>
<html lang="en">
<head>
<meta charset="utf-8">
<title>Corvalt Business Card</title>
<link rel="stylesheet" href="https://fonts.googleapis.com/css2?family=Open+Sans:wght@400;600;700;800&display=swap">
<style>
  :root {
    --backdrop: #2a2624;
    --card-black: #121212;
    --card-edge: #1e1e1e;
    --brand-red: #e8222a;
    --text-white: #f2f2f2;
    --text-grey: #cfcfcf;
    --uv-grey: #5a5a5a;
  }
  * { margin: 0; padding: 0; box-sizing: border-box; }
  html, body {
    width: 1200px;
    height: 716px;
    overflow: hidden;
    background: var(--backdrop);
    font-family: "Open Sans", Arial, sans-serif;
  }
  .canvas {
    position: relative;
    width: 1200px;
    height: 716px;
  }
  .card {
    position: absolute;
    top: 200px;
    width: 510px;
    height: 300px;
    background: var(--card-black);
    border: 1px solid var(--card-edge);
    border-radius: 4px;
  }
  .card--front { left: 60px; }
  .card--back { left: 630px; }

  /* Front side */
  .contact {
    position: absolute;
    left: 34px;
    top: 70px;
    font-size: 11px;
    line-height: 17px;
    color: var(--text-grey);
  }
  .contact__company {
    color: var(--brand-red);
    font-weight: 700;
  }
  .contact__row {
    display: flex;
    align-items: center;
    gap: 7px;
  }
  .contact__icon {
    width: 11px;
    height: 11px;
    flex: none;
    background: var(--brand-red);
    border-radius: 2px;
    display: flex;
    align-items: center;
    justify-content: center;
  }
  .contact__icon svg { width: 8px; height: 8px; }

  .identity {
    position: absolute;
    left: 290px;
    top: 62px;
  }
  .identity__brand {
    font-size: 34px;
    font-weight: 800;
    letter-spacing: 0.5px;
    color: var(--text-white);
    line-height: 1;
  }
  .identity__name {
    margin-top: 12px;
    font-size: 14px;
    font-weight: 700;
    letter-spacing: 1px;
    color: var(--brand-red);
  }
  .identity__role {
    margin-top: 2px;
    font-size: 11px;
    color: var(--text-grey);
  }

  /* Back side */
  .back-brand {
    position: absolute;
    inset: 0;
    display: flex;
    align-items: center;
    justify-content: center;
    font-size: 56px;
    font-weight: 800;
    letter-spacing: 1px;
    color: var(--uv-grey);
  }
</style>
</head>
<body>
<main class="canvas">

  <section class="card card--front" aria-label="Card front">
    <div class="contact">
      <p class="contact__company">Corvalt NZ Limited</p>
      <p>1100 Harbour Street</p>
      <p>Any where, Any City</p>
      <p class="contact__row">
        <span class="contact__icon">
          <svg viewBox="0 0 10 10"><path d="M2 1l2 2-1 1.2c.6 1.2 1.6 2.2 2.8 2.8L7 6l2 2-1.3 1.3C4.5 9 1 5.5.7 2.3z" fill="#fff"/></svg>
        </span>+64 027 604 91352
      </p>
      <p class="contact__row">
        <span class="contact__icon">
          <svg viewBox="0 0 10 10"><rect x="1" y="2.5" width="8" height="5" fill="none" stroke="#fff" stroke-width="1"/><path d="M1 2.5l4 3 4-3" fill="none" stroke="#fff" stroke-width="1"/></svg>
        </span>mark.pell@corvalt-example.co.nz
      </p>
      <p class="contact__row">
        <span class="contact__icon">
          <svg viewBox="0 0 10 10"><circle cx="5" cy="5" r="3.8" fill="none" stroke="#fff" stroke-width="1"/><path d="M1.2 5h7.6M5 1.2c-2 2.3-2 5.3 0 7.6M5 1.2c2 2.3 2 5.3 0 7.6" fill="none" stroke="#fff" stroke-width=".8"/></svg>
        </span>www.corvalt-example.co.nz
      </p>
    </div>

    <div class="identity">
      <p class="identity__brand">CORVALT</p>
      <p class="identity__name">MARK PELL</p>
      <p class="identity__role">Managing Director</p>
    </div>
  </section>

  <section class="card card--back" aria-label="Card back">
    <p class="back-brand">CORVALT</p>
  </section>

</main>
</body>
</html>
```